Web site for new fundraising service for charities

We need a web design for a new charitable trust based in New Zealand. With the economic downturn, charities are finding it increasingly difficult to raise the monies they need to deliver their services.

Using a network of fundraisers working out of their homes, BrightLot (our charitable trust) will source unique, high interest auction items on behalf of multiple charities - things like luxury cruises, exotic travel, luxury accommodation, fine dining, unique experiences with sports and entertainment personalities, tickets to sporting and entertainment events, etc.

Once we have sourced sufficient high value items we will then partner with Bidora (NZ's equivalent of Vendix) to launch the auction. The proceeds from each auction will benefit up to 6 charities. The auctions will be promoted through Bidora, through PR, and through the communications channels of the benefiting charities, reaching a wider audience than would be possible if just one charity was holding an auction and therefore resulting in more competitive bidding and higher returns for the charities.

We need a web site that we can point potential donors of auction items to, that gives them confidence in BrightLot. We will also leverage the web site with journalists. And of course, charities who are wondering whether or not to use BrightLot will come to our web site and check out our credentials. The tone of the site needs to be warm, friendly, approachable.

We are not locked into the blue and orange colors of the logo and in fact are experimenting with other colors as we speak.

Please note that what we're looking for is the design for the home page, plus a sub page design.

Target Market(s)

CEOs, corporate social responsibility managers, general managers, business owners, charities, the media

Industry/Entity Type

Communications

Requirements
Must have
• Video on home page
Newsletter sign up on all pages
Navigation as per the attached PDF example

```html
<!DOCTYPE html>
<html lang="en">
<head>
<meta charset="utf-8">
<title>BrightLot – Sharing Goodness</title>
<link href="https://fonts.googleapis.com/css2?family=Comic+Neue:wght@700&family=Arimo:wght@400;700&display=swap" rel="stylesheet">
<style>
  :root {
    --navy: #1b4688;
    --navy-dark: #133670;
    --navy-light: #7d93bd;
    --gold: #dc9422;
    --gold-deep: #cc9933;
    --white: #ffffff;
    --ink-blue: #3d5a94;
    --sky: #3f74c8;
    --sky-light: #8fb4e4;
    --page-bg: #ffffff;
  }
  * { box-sizing: border-box; margin: 0; padding: 0; }
  html, body { width: 1200px; height: 750px; overflow: hidden; background: var(--page-bg); }
  body { position: relative; font-family: "Comic Neue", "Comic Sans MS", cursive; }

  .site {
    position: absolute; left: 204px; top: 22px; width: 771px; height: 714px;
    background: linear-gradient(to bottom, var(--white) 0, var(--white) 550px, #d6deea 600px, #7d93bd 660px, var(--navy) 714px);
    box-shadow: 4px 4px 6px rgba(0,0,0,.35);
  }

  .brand { position: absolute; left: 24px; top: 8px; }
  .brand-mark { position: absolute; left: 72px; top: 4px; width: 62px; height: 62px; border-radius: 50%; background: var(--gold); }
  .brand-name {
    position: absolute; left: 0; top: 72px; white-space: nowrap;
    font-family: "Arimo", Arial, sans-serif; font-weight: 700; font-size: 50px;
    color: var(--navy); letter-spacing: -1px;
  }
  .brand-tagline {
    position: absolute; left: 10px; top: 126px; white-space: nowrap;
    font-family: "Arimo", Arial, sans-serif; font-size: 28px; color: var(--ink-blue);
  }

  .btn-text {
    color: var(--white); font-weight: 700;
    text-shadow: 1px 1px 0 var(--navy-dark), -1px -1px 0 var(--navy-dark), 1px -1px 0 var(--navy-dark), -1px 1px 0 var(--navy-dark), 2px 2px 3px rgba(0,0,0,.6);
  }

  .top-nav {
    position: absolute; left: 295px; top: 105px; width: 435px; height: 46px;
    border-radius: 8px;
    background: linear-gradient(160deg, var(--navy-light) 0, #5a76ad 40%, var(--navy) 55%);
    padding: 5px;
  }
  .top-nav-inner {
    height: 100%; border: 2px solid var(--white); border-radius: 6px;
    display: flex; gap: 38px; padding-left: 80px; align-items: center;
  }
  .top-nav a { font-size: 20px; text-decoration: none; }
  .top-nav-reflection {
    position: absolute; left: 295px; top: 152px; width: 435px; height: 38px;
    border-radius: 8px 8px 0 0;
    background: linear-gradient(to bottom, rgba(27,70,136,.45), rgba(255,255,255,0));
  }

  .side-nav { position: absolute; left: -9px; top: 201px; width: 155px; }
  .side-nav a {
    position: absolute; left: 0; width: 155px; height: 49px; display: block;
    text-decoration: none; border-radius: 0 6px 6px 0;
    background: radial-gradient(ellipse 140px 40px at 30px 4px, var(--navy-light) 70%, var(--navy) 72%);
    padding: 3px 6px 3px 0;
  }
  .side-nav a span {
    display: flex; height: 100%; align-items: center; justify-content: center;
    border: 2px solid var(--white); border-left: none; border-radius: 0 6px 6px 0;
    font-size: 17px; letter-spacing: -0.5px; white-space: nowrap; overflow: hidden;
    padding-left: 2px;
  }

  .video {
    position: absolute; left: 196px; top: 202px; width: 349px; height: 217px;
    background: radial-gradient(ellipse 260px 180px at 50% 45%, var(--sky-light) 0, var(--sky) 60%, var(--navy) 100%);
  }
  .video svg { position: absolute; left: 131px; top: 68px; }

  .quote-title { position: absolute; left: 196px; top: 445px; font-size: 26px; z-index: 2; white-space: nowrap; }
  .quote-box {
    position: absolute; left: 193px; top: 438px; width: 355px; height: 125px;
    border: 2px solid var(--gold-deep); border-radius: 3px;
    background: linear-gradient(to bottom, var(--white), var(--gold-deep));
  }

  .newsletter {
    position: absolute; left: 575px; top: 202px; width: 180px; height: 306px;
    border-radius: 8px;
    background: radial-gradient(ellipse 220px 100px at 70px 0, #5f7db5 80%, var(--navy) 82%);
    padding: 5px;
  }
  .newsletter-inner { height: 100%; border: 2px solid var(--white); border-radius: 6px; position: relative; }
  .newsletter h2 { font-size: 20px; text-align: center; line-height: 1.3; margin-top: 6px; letter-spacing: -0.3px; }
  .newsletter label { position: absolute; left: 28px; font-size: 20px; }
  .newsletter input {
    position: absolute; left: 18px; width: 140px; height: 26px; border: 1px solid #c8cfdb;
    background: linear-gradient(to bottom, #e4e6ea, var(--white) 40%);
  }
  .newsletter button {
    position: absolute; left: 16px; top: 206px; width: 146px; height: 54px;
    border: none; border-radius: 10px; background: var(--navy-dark);
    box-shadow: 2px 3px 4px rgba(0,0,0,.5); padding: 4px; font-family: inherit;
  }
  .newsletter button span {
    display: flex; height: 100%; align-items: center; justify-content: center;
    border: 2px solid var(--white); border-radius: 8px; background: var(--navy); font-size: 20px;
  }

  .copyright {
    position: absolute; left: 0; width: 771px; top: 686px; text-align: center;
    font-size: 16px; font-weight: 700; color: var(--white);
    text-shadow: 1px 1px 2px rgba(0,0,0,.4);
  }
</style>
</head>
<body>
  <div class="site">
    <header class="brand">
      <span class="brand-mark"></span>
      <span class="brand-name">BrightLot</span>
      <span class="brand-tagline">Sharing Goodness</span>
    </header>

    <nav class="top-nav">
      <div class="top-nav-inner">
        <a class="btn-text" href="#">Donors</a>
        <a class="btn-text" href="#">Charities</a>
        <a class="btn-text" href="#">Auctions</a>
      </div>
    </nav>
    <div class="top-nav-reflection"></div>

    <nav class="side-nav">
      <a href="#" style="top:0"><span class="btn-text">Home</span></a>
      <a href="#" style="top:55px"><span class="btn-text">How It Works</span></a>
      <a href="#" style="top:109px"><span class="btn-text">Acts Of Goodness</span></a>
      <a href="#" style="top:165px"><span class="btn-text">Goodness Partners</span></a>
      <a href="#" style="top:220px"><span class="btn-text">About</span></a>
      <a href="#" style="top:274px"><span class="btn-text">Contact</span></a>
    </nav>

    <div class="video" role="img" aria-label="Home page video: a luxury cruise ship at sea">
      <svg width="82" height="82" viewBox="0 0 82 82" aria-hidden="true">
        <circle cx="41" cy="41" r="40" fill="#ffffff"/>
        <polygon points="29,19 29,63 65,41" fill="#000000"/>
      </svg>
    </div>

    <div class="quote-box"></div>
    <h2 class="quote-title btn-text">Quote Of The Day</h2>

    <form class="newsletter">
      <div class="newsletter-inner">
        <h2 class="btn-text">Subscribe To Our Newsletter</h2>
        <label class="btn-text" style="top:70px">Name</label>
        <input type="text" style="top:99px" aria-label="Name">
        <label class="btn-text" style="top:137px">Email</label>
        <input type="email" style="top:166px" aria-label="Email">
        <button type="button"><span class="btn-text">Submit</span></button>
      </div>
    </form>

    <footer class="copyright">Copyright 2013 Your Website</footer>
  </div>
</body>
</html>
```